INCREASED BUDGET -- Cover Art Template Needed For Record Label

We are an electronic music record label that needs a cover art template for our 2017 releases. The design must be easy to update in Photoshop with different text, colors, or patterns.

The winner will also be asked to design our social media banners for Facebook, Twitter, and SoundCloud, so there's an opportunity to make more money.

Words to describe our sound: sophisticated, forward-thinking, futuristic, modern, emotional

Please make the HA logo the focal point of your design. Feel free to modify our logo as needed. Bonus points for anyone that can find a way to visually represent the word "Harborline". Examples of artwork that we found attractive are included to provide inspiration.

You can view our previous releases by clicking on any of the links: https://www.trackvendor-example.com/label/harborline-audio/52741/releases

Target Market(s)

Electronic music lovers

Industry/Entity Type

Music Download

Font styles to use
Serif
Decorative
Other font styles liked:
• Aller Display, Aller Light

Requirements
Must have
• Harborline Audio record logo
• Name of artist: Owen Tarsley
• Title: Daybreak / Stay Close (Remixes)
Nice to have
• Tracklist:
• Stay Close (Brannok Remix)
• Daybreak (Velktone Remix)
• Catalog number: 382

```html
<!DOCTYPE html>
<html lang="en">
<head>
<meta charset="utf-8">
<title>Owen Tarsley – Daybreak / Stay Close (Remixes) – Harborline Audio</title>
<link rel="stylesheet" href="https://fonts.googleapis.com/css2?family=Josefin+Sans:wght@300;400&display=swap">
<style>
  :root {
    --backdrop: #d3d5d2;
    --space-deep: #03121c;
    --space-mid: #0a3d52;
    --nebula: #1b8fb0;
    --nebula-glow: #44c6e0;
    --planet-dark: #061c26;
    --planet-light: #3fb3c9;
    --ring: rgba(225, 245, 250, 0.85);
    --type: #eef7fa;
  }
  * { margin: 0; padding: 0; box-sizing: border-box; }
  html, body {
    width: 1200px;
    height: 850px;
    overflow: hidden;
    background: var(--backdrop);
  }
  .stage {
    position: relative;
    width: 1200px;
    height: 850px;
  }
  .cover {
    position: absolute;
    left: 220px;
    top: 45px;
    width: 760px;
    height: 760px;
    overflow: hidden;
    background: var(--space-deep);
    font-family: "Josefin Sans", sans-serif;
    color: var(--type);
  }
  .cover-nebula {
    position: absolute;
    inset: 0;
    background:
      radial-gradient(ellipse 55% 45% at 50% 48%, rgba(68, 198, 224, 0.55), transparent 70%),
      radial-gradient(ellipse 40% 30% at 78% 30%, rgba(27, 143, 176, 0.55), transparent 75%),
      radial-gradient(ellipse 45% 35% at 22% 70%, rgba(27, 143, 176, 0.5), transparent 75%),
      radial-gradient(ellipse 70% 60% at 50% 50%, var(--space-mid), var(--space-deep) 90%);
  }
  .orbit-ring {
    position: absolute;
    left: 166px;
    top: 155px;
    width: 428px;
    height: 428px;
    border: 2px solid var(--ring);
    border-radius: 50%;
    box-shadow: inset 0 0 40px rgba(255, 255, 255, 0.12);
  }
  .planet {
    position: absolute;
    left: 235px;
    top: 183px;
    width: 356px;
    height: 356px;
    border-radius: 50%;
    background: radial-gradient(circle at 68% 58%, var(--planet-light), #1a6e84 45%, var(--planet-dark) 80%);
  }
  .release-info {
    position: absolute;
    left: 0;
    width: 760px;
    top: 290px;
    text-align: center;
  }
  .label-name {
    display: inline-block;
    font-size: 40px;
    font-weight: 400;
    letter-spacing: 2px;
    margin-bottom: 38px;
  }
  .release-title {
    font-size: 34px;
    font-weight: 300;
    letter-spacing: 2px;
    text-transform: uppercase;
    line-height: 1;
  }
  .release-subtitle {
    margin-top: 8px;
    font-size: 9px;
    font-weight: 300;
    letter-spacing: 3px;
    text-transform: uppercase;
  }
  .artist-name {
    margin-top: 14px;
    font-size: 17px;
    font-weight: 300;
    letter-spacing: 2px;
    text-transform: uppercase;
  }
</style>
</head>
<body>
<main class="stage">
  <section class="cover">
    <div class="cover-nebula" role="img" aria-label="Deep space with glowing turquoise nebula clouds and scattered stars"></div>
    <div class="planet" role="img" aria-label="Cracked turquoise planet glowing inside the orbit ring"></div>
    <div class="orbit-ring"></div>
    <div class="release-info">
      <div class="label-name">HA</div>
      <h1 class="release-title">Daybreak / Stay Close</h1>
      <p class="release-subtitle">(Remixes)</p>
      <p class="artist-name">Owen Tarsley</p>
    </div>
  </section>
</main>
</body>
</html>
```